Evaporative Air Conditioning Summer Service

Would like to design a flyer to send out in an email to existing clients to promote a Pre-summer service for Evaporative Air Conditioners
Cost will be $110.00 inc gst
Tasks included in service are
- Inspection and clean of pads
- Inspection and check float valve, water pump, fan, motor, bearings, drain
- Clean basin
- Supply of bacterial tablet
- Inspect overall condition of unit
- Any repairs if required will be quoted
Please see files attached of a previous very basic flyer I have used for installation and replacement unit costs. This has current contact information
Have also uploaded company logo for use.
Thanks

```html
<!DOCTYPE html>
<html lang="en">
<head>
<meta charset="UTF-8">
<title>Pre-Summer Evaporative Air Conditioner Service</title>
<link rel="stylesheet" href="https://fonts.googleapis.com/css2?family=Montserrat:wght@700;800;900&family=Poppins:wght@400;500;600;700&family=Oswald:wght@500;600&display=swap">
<style>
  :root {
    --blue: #1b5cb5;
    --blue-dark: #123f88;
    --orange: #f07f2a;
    --yellow: #f5c518;
    --grey-text: #555a60;
    --ink: #2b2e33;
    --page: #e2e2e2;
    --paper: #ffffff;
    --sky: #d6ebf8;
    --sand: #efe6d6;
  }
  * { box-sizing: border-box; margin: 0; padding: 0; }
  html, body { width: 1200px; height: 2496px; overflow: hidden; }
  body { background: var(--page); font-family: "Poppins", sans-serif; position: relative; }

  .flyer {
    position: absolute; left: 40px; top: 456px;
    width: 1120px; height: 1584px;
    background: var(--paper); overflow: hidden;
    box-shadow: 0 10px 30px rgba(0,0,0,.25);
  }
  .sky-wash {
    position: absolute; left: 0; top: 0; width: 1120px; height: 640px;
    background: linear-gradient(180deg, #e9f4fb 0%, #f7fbfe 60%, #ffffff 100%);
  }
  .hero-photo {
    position: absolute; left: 560px; top: 0; width: 560px; height: 600px;
    background: linear-gradient(180deg, #cfe6f6 0%, #dcecf6 45%, #eee5d4 70%, #f2ebdf 100%);
    -webkit-mask-image: linear-gradient(90deg, transparent 0%, #000 30%);
    mask-image: linear-gradient(90deg, transparent 0%, #000 30%);
  }
  .swoosh { position: absolute; left: 0; top: 0; }

  .brand {
    position: absolute; left: 70px; top: 80px;
    display: flex; align-items: center; gap: 16px;
  }
  .brand-dot { width: 54px; height: 54px; border-radius: 50%; background: var(--orange); }
  .brand-name {
    font-family: "Poppins", sans-serif; font-weight: 700; font-size: 40px;
    color: var(--blue); letter-spacing: .5px; line-height: 1;
  }

  .headline { position: absolute; left: 70px; top: 205px; }
  .headline .pre {
    font-family: "Montserrat", sans-serif; font-weight: 900; font-size: 60px;
    color: var(--blue); line-height: 1; letter-spacing: 1px;
  }
  .headline .sub {
    font-family: "Montserrat", sans-serif; font-weight: 700; font-size: 30px;
    color: var(--orange); line-height: 1.1; letter-spacing: 1.5px; margin-top: 4px;
  }
  .headline .main {
    font-family: "Montserrat", sans-serif; font-weight: 800; font-size: 51px;
    color: var(--grey-text); line-height: 1.1; letter-spacing: .5px;
  }

  .price-badge { position: absolute; left: 55px; top: 375px; width: 240px; height: 240px; }
  .price-text {
    position: absolute; left: 55px; top: 375px; width: 240px; height: 240px;
    display: flex; flex-direction: column; align-items: center; justify-content: center;
    color: #fff; transform: rotate(-6deg);
  }
  .price-text .label { font-family: "Oswald", sans-serif; font-weight: 500; font-size: 28px; line-height: 1; }
  .price-text .amount { font-family: "Oswald", sans-serif; font-weight: 600; font-size: 82px; line-height: 1; }
  .price-text .amount sup { font-size: 38px; vertical-align: 30px; margin-right: 2px; }
  .price-text .tax { font-family: "Poppins", sans-serif; font-size: 18px; line-height: 1.1; }

  .worker-photo {
    position: absolute; left: 500px; top: 700px; width: 620px; height: 884px;
    background: linear-gradient(160deg, #eef1f4 0%, #d9dee4 30%, #3a6fc0 55%, #4a4f58 80%, #3c4048 100%);
    -webkit-mask-image: linear-gradient(90deg, transparent 0%, #000 25%);
    mask-image: linear-gradient(90deg, transparent 0%, #000 25%);
  }

  .tasks-title {
    position: absolute; left: 70px; top: 645px;
    font-family: "Poppins", sans-serif; font-weight: 600; font-size: 32px; color: var(--ink);
  }
  .tasks-dots { position: absolute; left: 72px; top: 695px; display: flex; gap: 5px; }
  .tasks-dots span { width: 6px; height: 6px; border-radius: 50%; background: var(--orange); }

  .task-list { position: absolute; left: 70px; top: 0; list-style: none; }
  .task {
    position: absolute; left: 0; width: 440px;
    display: flex; align-items: flex-start; gap: 14px;
    font-size: 22px; line-height: 1.13; color: var(--grey-text);
  }
  .task svg { flex: 0 0 34px; width: 34px; height: 34px; margin-top: -4px; }

  .gallery-photo {
    position: absolute; width: 212px; height: 212px; border-radius: 50%;
    border: 7px solid var(--blue);
  }
  .g1 { left: 76px; top: 1081px; background: radial-gradient(circle at 45% 40%, #f3f3f3 0%, #d9c7a5 55%, #b5874a 100%); }
  .g2 { left: 312px; top: 1081px; background: radial-gradient(circle at 55% 45%, #cfd5db 0%, #7b8794 55%, #2a2d33 100%); }
  .g3 { left: 548px; top: 1081px; background: radial-gradient(circle at 50% 45%, #e7e9ec 0%, #9aa7bb 50%, #2f5fb0 100%); }

  .cta-get {
    position: absolute; left: 78px; top: 1345px;
    font-family: "Montserrat", sans-serif; font-weight: 700; font-size: 56px; color: var(--orange);
  }
  .cta-banner { position: absolute; left: 245px; top: 1329px; }
  .cta-text {
    position: absolute; left: 300px; top: 1343px;
    font-family: "Montserrat", sans-serif; font-weight: 800; font-size: 57px;
    color: #fff; letter-spacing: 1px; line-height: 1.15;
  }

  .contact {
    position: absolute; top: 1436px; left: 80px;
    display: flex; gap: 40px; font-size: 22px; color: var(--ink); font-weight: 500;
  }
  .contact span { display: flex; align-items: center; gap: 6px; }
  .contact svg { width: 18px; height: 18px; }
  .website {
    position: absolute; left: 80px; top: 1475px;
    font-family: "Poppins", sans-serif; font-weight: 500; font-size: 33px;
    letter-spacing: 2.5px; color: var(--ink);
  }
  .website .domain { color: var(--orange); font-weight: 600; }
</style>
</head>
<body>
<main class="flyer">
  <div class="sky-wash"></div>
  <div class="hero-photo" role="img" aria-label="Evaporative and split air conditioner units with a straw hat on a sunny beach"></div>

  <svg class="swoosh" width="1120" height="720" viewBox="0 0 1120 720" aria-hidden="true">
    <defs>
      <linearGradient id="swooshFill" x1="0" y1="0" x2="1" y2="0">
        <stop offset="0" stop-color="#ee6f2a"/>
        <stop offset=".6" stop-color="#f39a26"/>
        <stop offset="1" stop-color="#f6cf16"/>
      </linearGradient>
    </defs>
    <path d="M 280 465 C 470 520, 640 640, 1120 545 L 1120 625 C 720 690, 520 620, 280 478 Z" fill="url(#swooshFill)"/>
  </svg>

  <div class="brand">
    <span class="brand-dot"></span>
    <span class="brand-name">HARBOURLINE</span>
  </div>

  <header class="headline">
    <h1 class="pre">PRE–SUMMER</h1>
    <p class="sub">SERVICE FOR EVAPORATIVE</p>
    <p class="main">AIR CONDITIONERS</p>
  </header>

  <svg class="price-badge" viewBox="0 0 240 240" aria-hidden="true">
    <circle cx="120" cy="120" r="116" fill="none" stroke="#1b5cb5" stroke-width="8" stroke-dasharray="6 5"/>
    <circle cx="120" cy="120" r="110" fill="#1b5cb5"/>
    <circle cx="120" cy="120" r="100" fill="none" stroke="#3f7bd0" stroke-width="2"/>
  </svg>
  <div class="price-text">
    <span class="label">COST WILL BE</span>
    <span class="amount"><sup>$</sup>110</span>
    <span class="tax">INC GST</span>
  </div>

  <div class="worker-photo" role="img" aria-label="Technician in blue cap and overalls servicing a wall-mounted air conditioner"></div>

  <h2 class="tasks-title">Tasks included in our service are</h2>
  <div class="tasks-dots"><span></span><span></span><span></span><span></span></div>

  <ul class="task-list">
    <li class="task" style="top:722px">
      <svg viewBox="0 0 34 34" fill="none" stroke="#1b5cb5" stroke-width="2"><rect x="6" y="5" width="22" height="26" rx="2"/><rect x="12" y="2" width="10" height="6" rx="1"/><path d="M10 14h14M10 19h14M10 24h10"/></svg>
      <span>Inspection and clean of pads</span>
    </li>
    <li class="task" style="top:793px">
      <svg viewBox="0 0 34 34" fill="none" stroke="#1b5cb5" stroke-width="2"><rect x="4" y="16" width="18" height="14"/><circle cx="13" cy="23" r="3"/><path d="M22 20h8M17 16v-6h8M25 6v8"/></svg>
      <span>Inspection and check float valve, water pump, fan, motor, bearings, drain</span>
    </li>
    <li class="task" style="top:880px">
      <svg viewBox="0 0 34 34" fill="none" stroke="#1b5cb5" stroke-width="2"><path d="M4 17h26c0 7-5 11-13 11S4 24 4 17z"/><path d="M17 17V7h7M24 7v4"/></svg>
      <span>Clean basin</span>
    </li>
    <li class="task" style="top:929px">
      <svg viewBox="0 0 34 34" fill="none" stroke="#1b5cb5" stroke-width="2"><circle cx="17" cy="17" r="13"/><path d="M8 8l18 18M12 17a5 5 0 1 0 10 0a5 5 0 1 0-10 0"/></svg>
      <span>Supply of bacterial tablet</span>
    </li>
    <li class="task" style="top:978px">
      <svg viewBox="0 0 34 34" fill="none" stroke="#1b5cb5" stroke-width="2"><path d="M18 3L9 18h7l-3 13 11-17h-7l4-11z"/></svg>
      <span>Inspect overall condition of unit</span>
    </li>
    <li class="task" style="top:1027px">
      <svg viewBox="0 0 34 34" fill="none" stroke="#1b5cb5" stroke-width="2"><path d="M4 6h12v8h8v14h-6v-8h-8v-6H4z"/></svg>
      <span>Any repairs if required will be quoted</span>
    </li>
  </ul>

  <div class="gallery-photo g1" role="img" aria-label="Technician servicing a water heater unit"></div>
  <div class="gallery-photo g2" role="img" aria-label="Technician cleaning a split system air conditioner"></div>
  <div class="gallery-photo g3" role="img" aria-label="Technician testing an outdoor unit with a multimeter"></div>

  <p class="cta-get">Get a</p>
  <svg class="cta-banner" width="660" height="98" viewBox="0 0 660 98" aria-hidden="true">
    <polygon points="14,0 660,0 660,98 14,98 40,49" fill="#1b5cb5"/>
    <polygon points="0,0 14,0 40,49 14,98 0,98 26,49" fill="#123f88"/>
  </svg>
  <p class="cta-text">FREE ESTIMATE</p>

  <div class="contact">
    <span><svg viewBox="0 0 18 18" fill="none" stroke="#1b5cb5" stroke-width="2"><path d="M4 2l3 3-2 3c1 2 3 4 5 5l3-2 3 3-2 3C7 17 1 11 2 4z"/></svg>0400 555 018</span>
    <span><svg viewBox="0 0 18 18"><rect x="1" y="4" width="16" height="11" fill="#1b5cb5"/><path d="M1 4l8 6 8-6" fill="none" stroke="#fff" stroke-width="1.5"/></svg>admin@harbourlinegasplumbing.com.au</span>
  </div>
  <p class="website">www.<span class="domain">harbourlinegasplumbing</span>.com.au</p>
</main>
</body>
</html>
```